SipLoop Business Cards

Hi designers!

Here's some background on our start-up and this project:

SipLoop is a website that will allow users to order alcohol from nearby liquor stores and have it delivered to their homes in minutes. We are really excited to work on creating the best online, alcohol purchasing experience for the users.

So why SipLoop? We like to think of ourselves as that great friend who will get alcohol for you because he happens to have a car. We help you drink in with your friends, family, or guests. Our site will target students and young professionals (of drinking age) who are comfortable buying things online or through apps. We don't see this service as a luxury, VIP, or niche service in the least; instead, we think of us as a relaxed, service-driven start-up that believes in simple design and transparent .

Now, we want a business card that incorporates our newly acquired logo design and some complimenting colors and fonts. Feel free to do it single or double sided, although I'm a sucker for double...

If you happen to have any questions, want to throw some ideas around, or just want some feedback- email me at marco@siploop.example.

Marco Tessin
Founder

Industry/Entity Type

Business

Requirements
Must have
• Name, Position, Email, Cell-phone

No address, no fax, no land-line.

```html
<!DOCTYPE html>
<html lang="en">
<head>
<meta charset="utf-8">
<title>SipLoop Business Cards</title>
<link rel="stylesheet" href="https://fonts.googleapis.com/css2?family=Poppins:wght@300;400;800&display=swap">
<style>
  :root {
    --backdrop: #d9d9d9;
    --card-white: #ffffff;
    --card-dark: #2b2b2b;
    --ink-dark: #232323;
    --ink-light: #f2f2f2;
    --accent: #f2c200;
    --rule: #8a8a8a;
  }
  * { margin: 0; padding: 0; box-sizing: border-box; }
  html, body {
    width: 1200px;
    height: 900px;
    overflow: hidden;
    background: var(--backdrop);
    font-family: "Poppins", sans-serif;
  }
  .sheet {
    width: 1200px;
    height: 900px;
    display: flex;
    flex-direction: column;
    align-items: center;
    justify-content: center;
    gap: 60px;
  }
  .card {
    position: relative;
    width: 630px;
    height: 360px;
    box-shadow: 0 10px 30px rgba(0,0,0,0.22);
  }
  .card--front {
    background: var(--card-white);
    display: flex;
    align-items: center;
    justify-content: center;
  }
  .card--back {
    background: var(--card-dark);
    color: var(--ink-light);
  }
  .wordmark {
    display: flex;
    align-items: center;
    gap: 14px;
    font-weight: 800;
    letter-spacing: -2px;
    line-height: 1;
  }
  .wordmark__dot {
    width: 0.28em;
    height: 0.28em;
    border-radius: 50%;
    background: var(--accent);
  }
  .card--front .wordmark {
    font-size: 96px;
    color: var(--ink-dark);
  }
  .card--back .wordmark {
    position: absolute;
    left: 180px;
    top: 34px;
    font-size: 64px;
    color: var(--ink-light);
  }
  .contact-list {
    position: absolute;
    left: 36px;
    top: 128px;
    list-style: none;
    font-size: 12px;
    font-weight: 300;
  }
  .contact-list li {
    display: flex;
    align-items: center;
    gap: 8px;
    height: 18px;
  }
  .contact-icon {
    width: 12px;
    height: 12px;
    flex: none;
  }
  .divider {
    position: absolute;
    left: 36px;
    right: 40px;
    top: 206px;
    height: 1px;
    background: var(--rule);
  }
  .person {
    position: absolute;
    right: 40px;
    top: 250px;
    text-align: right;
  }
  .person__name {
    font-size: 16px;
    font-weight: 300;
    letter-spacing: 0.5px;
    padding-bottom: 6px;
    border-bottom: 1px solid var(--rule);
  }
  .person__role {
    margin-top: 5px;
    font-size: 13px;
    font-weight: 400;
    color: var(--accent);
  }
</style>
</head>
<body>
<main class="sheet">
  <section class="card card--front" aria-label="Business card front">
    <div class="wordmark">SipLoop<span class="wordmark__dot"></span></div>
  </section>

  <section class="card card--back" aria-label="Business card back">
    <div class="wordmark">SipLoop<span class="wordmark__dot"></span></div>

    <ul class="contact-list">
      <li>
        <svg class="contact-icon" viewBox="0 0 12 12" aria-hidden="true">
          <rect width="12" height="12" fill="var(--accent)"/>
          <path d="M3.5 2.5l1.5 0 .6 1.8-1 .7c.5 1 1.2 1.7 2.2 2.2l.7-1 1.8.6v1.5c0 .4-.4.7-.8.7C5.6 8.8 3 6.2 2.8 3.3c0-.4.3-.8.7-.8z" fill="var(--card-dark)"/>
        </svg>
        <span>0555 010 010</span>
      </li>
      <li>
        <svg class="contact-icon" viewBox="0 0 12 12" aria-hidden="true">
          <rect width="12" height="12" fill="var(--accent)"/>
          <rect x="2.5" y="3.5" width="7" height="5" fill="none" stroke="var(--card-dark)" stroke-width="1"/>
          <path d="M2.5 3.5L6 6.3l3.5-2.8" fill="none" stroke="var(--card-dark)" stroke-width="1"/>
        </svg>
        <span>marco@siploop.example</span>
      </li>
      <li>
        <svg class="contact-icon" viewBox="0 0 12 12" aria-hidden="true">
          <rect width="12" height="12" fill="var(--accent)"/>
          <circle cx="6" cy="6" r="3.3" fill="none" stroke="var(--card-dark)" stroke-width="1"/>
          <path d="M2.7 6h6.6M6 2.7c-1.6 2-1.6 4.6 0 6.6M6 2.7c1.6 2 1.6 4.6 0 6.6" fill="none" stroke="var(--card-dark)" stroke-width="0.8"/>
        </svg>
        <span>www.siploop.example</span>
      </li>
    </ul>

    <div class="divider"></div>

    <div class="person">
      <p class="person__name">MARCO TESSIN</p>
      <p class="person__role">President</p>
    </div>
  </section>
</main>
</body>
</html>
```